Web design required

1-We need a web design for existing company based in New Zealand
2-We build residential house and light commercial
3-We has in-house designer which allow us can provide interior design
4-We modeling project before site construction, which enable both client and construction team to visually analysis whole project,

Target Market(s)

middle class residential house market
Ref: http://www.brambleworthbuilders.co.nz/

Industry/Entity Type

Construction Company

Number of Pages Required

1 page

Font styles to use
Sans Serif
Other font styles liked:
• Such as : Central Gothic or similar which has more design taste

Colors

Designer to choose colors to be used in the design.

Requirements
Must have
• Front sheet, contact information, sample project

```html
<!DOCTYPE html>
<html lang="en">
<head>
<meta charset="utf-8">
<title>Harrowfield Homes</title>
<link href="https://fonts.googleapis.com/css2?family=Montserrat:wght@400;600;700&family=Questrial&display=swap" rel="stylesheet">
<style>
:root{
  --blue:#1a63b5;
  --blue-dark:#0f4589;
  --navy:#0d2440;
  --ink:#2b2b2b;
  --muted:#7a7f87;
  --line:#d7dde5;
  --white:#ffffff;
  --footer:#1b232d;
}
*{box-sizing:border-box;margin:0;padding:0}
html,body{width:1200px;height:2560px;overflow:hidden}
body{font-family:"Questrial",Arial,sans-serif;color:var(--ink);background:var(--white);position:relative}
.btn{display:inline-block;font-family:"Montserrat",sans-serif;font-weight:600;font-size:12px;letter-spacing:1px;padding:10px 22px;border-radius:20px}
.btn-solid{background:var(--blue);color:var(--white)}
.btn-outline{border:1.5px solid var(--blue);color:var(--blue);background:var(--white)}

/* hero */
.hero{position:absolute;top:0;left:0;width:1200px;height:520px;overflow:hidden}
.hero-photo{position:absolute;inset:0;background:linear-gradient(180deg,#5f7590 0%,#8296ac 40%,#5d6469 70%,#3a3f43 100%)}
.hero-shade{position:absolute;inset:0;background:rgba(10,20,35,.35)}
.hero-accent{position:absolute;inset:0}
.site-nav{position:absolute;top:0;left:0;width:100%;height:70px;display:flex;align-items:center;padding:0 90px}
.brand{display:flex;align-items:center;gap:10px;font-family:"Montserrat",sans-serif;font-weight:700;font-size:22px;color:var(--white);letter-spacing:1px}
.brand-mark{width:24px;height:24px;background:var(--white)}
.menu{margin-left:auto;display:flex;gap:0;align-items:center}
.menu a{font-family:"Montserrat",sans-serif;font-size:12px;font-weight:600;color:var(--white);letter-spacing:1px;padding:26px 18px;text-decoration:none}
.menu a.active{background:var(--blue)}
.menu svg{margin-left:16px}
.hero-title{position:absolute;top:185px;width:100%;text-align:center;color:var(--white)}
.hero-title h1{font-family:"Montserrat",sans-serif;font-size:58px;font-weight:700;letter-spacing:2px}
.hero-title p{font-size:20px;margin-top:8px}
.hero-down{position:absolute;left:577px;top:428px}

/* welcome */
.welcome{position:absolute;top:520px;left:0;width:1200px;height:660px}
.welcome-box{position:absolute;left:100px;top:80px;width:530px;height:300px;border:1px solid var(--line);padding:30px 36px}
.welcome-box h2{font-family:"Montserrat",sans-serif;font-size:28px;font-weight:600;color:var(--navy);margin-bottom:22px}
.welcome-box p{font-size:13px;line-height:1.75;color:var(--muted);margin-bottom:14px;max-width:380px}
.welcome .btn{position:absolute;left:148px;top:410px}
.welcome-media{position:absolute;left:585px;top:80px;width:515px;height:392px;background:linear-gradient(135deg,#e8edf2,#c9d2dc 60%,#aab4bf)}
.play{position:absolute;left:232px;top:170px}

/* services */
.services{position:absolute;top:1180px;left:0;width:1200px;height:540px;overflow:hidden}
.services-photo{position:absolute;inset:0;background:linear-gradient(180deg,#2a6cbd,#1c5aa6 60%,#174d91)}
.services h2{position:absolute;top:70px;width:100%;text-align:center;font-family:"Montserrat",sans-serif;font-size:26px;font-weight:600;color:var(--white)}
.card{position:absolute;top:135px;width:300px;height:325px;background:#f4f6f9;text-align:center;padding:40px 26px 0}
.card h3{font-family:"Montserrat",sans-serif;font-size:17px;font-weight:600;color:var(--navy);margin:22px 0 16px;line-height:1.3}
.card p{font-size:12px;line-height:1.7;color:var(--muted);margin-bottom:18px}
.card .btn{font-size:10px;padding:7px 18px}

/* gallery */
.gallery{position:absolute;top:1740px;left:0;width:1200px;height:256px;display:flex;gap:6px}
.shot{flex:1;height:100%}
.g-arrow{position:absolute;top:110px;width:24px;height:36px;background:rgba(0,0,0,.45);display:flex;align-items:center;justify-content:center}

/* footer */
.footer{position:absolute;top:1996px;left:0;width:1200px;height:564px;overflow:hidden}
.footer-photo{position:absolute;inset:0;background:linear-gradient(180deg,#2d3744,#1d252f 50%,#141a21)}
.footer-wave{position:absolute;top:0;left:0}
.to-top{position:absolute;top:48px;left:0;width:100%;text-align:center;font-family:"Montserrat",sans-serif;font-size:11px;color:var(--white);letter-spacing:1px}
.footer h4{font-family:"Montserrat",sans-serif;font-size:20px;font-weight:600;color:var(--white);position:absolute;top:150px}
.form{position:absolute;left:96px;top:200px;width:612px}
.row{display:flex;gap:12px;margin-bottom:12px}
.field{flex:1;height:34px;background:var(--white);font-size:11px;color:#999;padding:10px 12px}
.field.tall{height:110px}
.form .btn{position:absolute;right:0;top:224px;border-radius:18px;font-size:11px;padding:9px 22px}
.info{position:absolute;left:780px;top:205px;width:330px}
.info li{list-style:none;display:flex;align-items:center;gap:18px;color:#c9d0d8;font-size:12px;height:46px}
.socials{display:flex;gap:10px;margin:12px 0 0 44px}
.socials span{width:26px;height:26px;border-radius:50%;background:var(--blue)}
.copy{position:absolute;top:520px;width:100%;text-align:center;font-size:11px;color:#8a939d}
</style>
</head>
<body>

<header class="hero">
  <div class="hero-photo" role="img" aria-label="Photograph of a modern two-storey family home at dusk"></div>
  <div class="hero-shade"></div>
  <svg class="hero-accent" width="1200" height="520" viewBox="0 0 1200 520">
    <polygon points="0,380 640,520 0,520" fill="#1a63b5" opacity=".85"/>
    <polygon points="0,470 420,520 0,520" fill="#0f4589"/>
  </svg>
  <nav class="site-nav">
    <div class="brand"><span class="brand-mark"></span>HARROWFIELD HOMES</div>
    <div class="menu">
      <a class="active">HOME</a><a>SERVICES</a><a>ABOUT</a><a>PROJECTS</a><a>CONTACT</a>
      <svg width="16" height="16" viewBox="0 0 16 16"><circle cx="6.5" cy="6.5" r="5" fill="none" stroke="#fff" stroke-width="2"/><line x1="10.5" y1="10.5" x2="15" y2="15" stroke="#fff" stroke-width="2"/></svg>
    </div>
  </nav>
  <div class="hero-title">
    <h1>HARROWFIELD HOMES</h1>
    <p>We build residential house and light commercial</p>
  </div>
  <svg class="hero-down" width="46" height="46" viewBox="0 0 46 46"><circle cx="23" cy="23" r="21" fill="none" stroke="#fff" stroke-width="2"/><polyline points="15,19 23,27 31,19" fill="none" stroke="#fff" stroke-width="2"/></svg>
</header>

<section class="welcome">
  <div class="welcome-box">
    <h2>Welcome to Harrowfield Homes</h2>
    <p>Harrowfield Homes is dedicated to creating and renovating beautiful and unusual buildings.</p>
    <p>Our team works with you to take dream houses off the blueprints and into reality. We have the knowledge and expertise to customise homes to suit you, from unusual materials and designs to environmentally sensitive locations.</p>
  </div>
  <span class="btn btn-solid">READ MORE</span>
  <div class="welcome-media" role="img" aria-label="Photograph of an architect drawing house plans on a desk">
    <svg class="play" width="52" height="52" viewBox="0 0 52 52"><circle cx="26" cy="26" r="26" fill="#1b1b1b"/><polygon points="21,16 37,26 21,36" fill="#fff"/></svg>
  </div>
</section>

<section class="services">
  <div class="services-photo" role="img" aria-label="Blue-toned photograph of houses under construction"></div>
  <h2>Our Services</h2>
  <div class="card" style="left:90px">
    <svg width="70" height="60" viewBox="0 0 70 60"><rect x="6" y="4" width="58" height="52" fill="none" stroke="#1a63b5" stroke-width="4"/><line x1="6" y1="28" x2="40" y2="28" stroke="#1a63b5" stroke-width="4"/><line x1="40" y1="4" x2="40" y2="40" stroke="#1a63b5" stroke-width="4"/><rect x="14" y="36" width="14" height="10" fill="#1a63b5"/></svg>
    <h3>Preconstruction<br>Planning</h3>
    <p>We have the knowledge and expertise to customise homes to suit you, from unusual materials &amp; designs.</p>
    <span class="btn btn-outline">READ MORE</span>
  </div>
  <div class="card" style="left:450px">
    <svg width="70" height="60" viewBox="0 0 70 60"><polygon points="35,4 66,28 4,28" fill="#1a63b5"/><rect x="12" y="28" width="46" height="28" fill="none" stroke="#1a63b5" stroke-width="4"/><rect x="29" y="38" width="12" height="18" fill="#1a63b5"/></svg>
    <h3>Construction<br>Modelling</h3>
    <p>We have the knowledge and expertise to customise homes to suit you, from unusual materials &amp; designs.</p>
    <span class="btn btn-outline">READ MORE</span>
  </div>
  <div class="card" style="left:810px">
    <svg width="70" height="60" viewBox="0 0 70 60"><path d="M18 24 A17 17 0 0 1 52 24 Z" fill="#1a63b5"/><rect x="14" y="24" width="42" height="5" fill="#1a63b5"/><path d="M8 58 Q8 38 35 36 Q62 38 62 58 Z" fill="#1a63b5"/><circle cx="35" cy="31" r="0" fill="#1a63b5"/></svg>
    <h3>Full Project<br>Management</h3>
    <p>We have the knowledge and expertise to customise homes to suit you, from unusual materials &amp; designs.</p>
    <span class="btn btn-outline">READ MORE</span>
  </div>
</section>

<section class="gallery">
  <div class="shot" style="background:linear-gradient(160deg,#d9dcde,#9aa1a6)" role="img" aria-label="Photograph of a white villa exterior"></div>
  <div class="shot" style="background:linear-gradient(160deg,#8a6b4b,#e5ddd2)" role="img" aria-label="Photograph of a timber ceiling interior"></div>
  <div class="shot" style="background:linear-gradient(160deg,#eceae6,#b8b3ab)" role="img" aria-label="Photograph of a staircase interior"></div>
  <div class="shot" style="background:linear-gradient(160deg,#5e6a74,#2f3236)" role="img" aria-label="Photograph of a modern dark-clad house"></div>
  <div class="shot" style="background:linear-gradient(160deg,#b8c9da,#e8ebee)" role="img" aria-label="Photograph of a two-storey weatherboard home"></div>
  <div class="g-arrow" style="left:0"><svg width="10" height="14"><polyline points="8,1 2,7 8,13" fill="none" stroke="#fff" stroke-width="2"/></svg></div>
  <div class="g-arrow" style="right:0"><svg width="10" height="14"><polyline points="2,1 8,7 2,13" fill="none" stroke="#fff" stroke-width="2"/></svg></div>
</section>

<footer class="footer">
  <div class="footer-photo" role="img" aria-label="Dark photograph of a family home at night"></div>
  <svg class="footer-wave" width="1200" height="110" viewBox="0 0 1200 110">
    <path d="M0,0 H1200 V60 Q600,-10 0,60 Z" fill="#fff"/>
    <path d="M0,60 Q600,-10 1200,60 V80 Q600,10 0,80 Z" fill="#1a63b5"/>
    <polygon points="560,38 600,12 640,38" fill="#fff"/>
  </svg>
  <div class="to-top">TO TOP</div>
  <h4 style="left:96px">Contact form</h4>
  <h4 style="left:780px">Contact Information</h4>
  <div class="form">
    <div class="row"><div class="field">Name</div><div class="field">Phone</div></div>
    <div class="row"><div class="field">Email</div></div>
    <div class="row"><div class="field tall">Message</div></div>
    <span class="btn btn-solid">SUBMIT</span>
  </div>
  <ul class="info">
    <li><svg width="16" height="20" viewBox="0 0 16 20"><path d="M8 1 A7 7 0 0 1 15 8 C15 13 8 19 8 19 C8 19 1 13 1 8 A7 7 0 0 1 8 1 Z" fill="#c9d0d8"/><circle cx="8" cy="8" r="2.5" fill="#1b232d"/></svg>41 Kereru Lane, Hamilton 3204</li>
    <li><svg width="16" height="18" viewBox="0 0 16 18"><path d="M3 1 L6 1 L7 5 L5 7 Q7 11 10 13 L12 11 L15 12 L15 15 Q9 17 4 11 Q1 6 3 1 Z" fill="#c9d0d8"/></svg>0800 555 274</li>
    <li><svg width="18" height="14" viewBox="0 0 18 14"><rect x="1" y="1" width="16" height="12" fill="none" stroke="#c9d0d8" stroke-width="2"/><polyline points="1,1 9,8 17,1" fill="none" stroke="#c9d0d8" stroke-width="2"/></svg>info@harrowfieldhomes.co.nz</li>
  </ul>
  <div class="socials" style="position:absolute;left:780px;top:360px"><span></span><span></span><span></span><span></span></div>
  <div class="copy">Copyright © 2017 Harrowfield Homes. All rights reserved.</div>
</footer>

</body>
</html>
```